Bravel Acres Business Cards

design business cards for our new business should match my Corvane Quotations business cards

Contact Information for Business Card

2817 W 68th N St
Tulsa, OK 74592

Requirements
Must have
• should match logo colors

```html
<!DOCTYPE html>
<html lang="en">
<head>
<meta charset="utf-8">
<title>Bravel Acres – Business Cards</title>
<link rel="stylesheet" href="https://fonts.googleapis.com/css2?family=Montserrat:ital,wght@0,500;0,600;0,700;0,800;1,700&display=swap">
<style>
  :root{
    --green:#7cc242;
    --teal:#1fa8a6;
    --ink:#1f2a36;
    --paper:#ffffff;
    --backdrop:#e9ebec;
    --pattern:#eef1f1;
  }
  *{box-sizing:border-box;margin:0;padding:0}
  html,body{width:1200px;height:1200px;overflow:hidden;background:var(--backdrop);font-family:"Montserrat",sans-serif;color:var(--ink)}
  .sheet{position:relative;width:1200px;height:1200px}
  .card{position:absolute;left:160px;width:880px;height:537px;background:var(--paper);box-shadow:0 6px 18px rgba(0,0,0,.18);overflow:hidden}
  .card--front{top:43px}
  .card--back{top:620px}
  .card__bands{position:absolute;inset:0;width:100%;height:100%}
  .brand{position:absolute;display:flex;align-items:center;gap:16px}
  .brand__dot{width:34px;height:34px;border-radius:50%;background:var(--green);flex:none}
  .brand__name{font-weight:700;color:var(--ink);letter-spacing:.04em;white-space:nowrap}
  .card--front .brand{left:70px;top:240px}
  .card--front .brand__name{font-size:38px}
  .person{position:absolute;left:505px;top:192px}
  .person__name{font-weight:800;font-size:31px;letter-spacing:.06em;line-height:1;padding-bottom:4px;border-bottom:1.5px solid var(--teal);display:inline-block}
  .person__first{color:var(--green)}
  .person__last{color:var(--teal);margin-left:.35em}
  .person__role{font-weight:700;font-style:italic;font-size:18px;margin-top:6px}
  .contacts{position:absolute;left:505px;top:290px;list-style:none}
  .contacts li{display:flex;align-items:flex-start;gap:16px;font-weight:600;font-size:16px;line-height:1.3;margin-bottom:20px}
  .contacts svg{width:24px;height:24px;flex:none}
  .site{position:absolute;left:62px;bottom:13px;color:#fff;font-weight:700;font-size:19px;letter-spacing:.03em}
  .pattern{position:absolute;left:0;top:40px;width:560px;height:440px;background:linear-gradient(135deg,var(--pattern),#f7f8f8)}
  .card--back .brand{left:260px;top:225px}
  .card--back .brand__dot{width:46px;height:46px}
  .card--back .brand__name{font-size:52px}
</style>
</head>
<body>
<main class="sheet">

  <section class="card card--front" aria-label="Business card front">
    <svg class="card__bands" viewBox="0 0 820 500" preserveAspectRatio="none" aria-hidden="true">
      <polygon points="0,0 425,0 412,13 0,13" fill="var(--green)"/>
      <polygon points="430,0 820,0 820,40 395,40" fill="var(--teal)"/>
      <polygon points="0,447 368,447 410,500 0,500" fill="var(--green)"/>
      <polygon points="398,472 820,472 820,500 420,500" fill="var(--teal)"/>
    </svg>

    <div class="brand">
      <span class="brand__dot"></span>
      <span class="brand__name">BRAVEL ACRES</span>
    </div>

    <div class="person">
      <p class="person__name"><span class="person__first">MARA</span><span class="person__last">QUILL</span></p>
      <p class="person__role">President</p>
    </div>

    <ul class="contacts">
      <li>
        <svg viewBox="0 0 24 24" aria-hidden="true"><circle cx="12" cy="12" r="10.5" fill="none" stroke="var(--ink)" stroke-width="1.4"/><path d="M8.5 7.5l2 2-1 1.3c.7 1.4 1.8 2.5 3.2 3.2l1.3-1 2 2-1.4 1.5c-3.4-.4-6.7-3.7-7.1-7.1z" fill="var(--green)"/></svg>
        <span>555-014-2290</span>
      </li>
      <li>
        <svg viewBox="0 0 24 24" aria-hidden="true"><circle cx="12" cy="12" r="10.5" fill="none" stroke="var(--ink)" stroke-width="1.4"/><rect x="6.5" y="8" width="11" height="8" rx="1" fill="none" stroke="var(--green)" stroke-width="1.4"/><path d="M6.8 8.4L12 12.5l5.2-4.1" fill="none" stroke="var(--green)" stroke-width="1.4"/></svg>
        <span>MQuill@bravelacres.com</span>
      </li>
      <li>
        <svg viewBox="0 0 24 24" aria-hidden="true"><circle cx="12" cy="12" r="10.5" fill="none" stroke="var(--ink)" stroke-width="1.4"/><path d="M12 18s-4-4.3-4-7.2a4 4 0 018 0C16 13.7 12 18 12 18z" fill="var(--green)"/><circle cx="12" cy="10.8" r="1.5" fill="#fff"/></svg>
        <span>2817 W 68th N St<br>Tulsa, OK 74592</span>
      </li>
    </ul>

    <p class="site">WWW.BRAVELACRES.COM</p>
  </section>

  <section class="card card--back" aria-label="Business card back">
    <div class="pattern" role="img" aria-label="Faint repeated text pattern background"></div>
    <svg class="card__bands" viewBox="0 0 820 500" preserveAspectRatio="none" aria-hidden="true">
      <polygon points="520,0 820,0 820,55 470,55" fill="var(--teal)"/>
      <polygon points="0,455 330,455 370,500 0,500" fill="var(--green)"/>
      <polygon points="420,440 820,440 820,470 445,470" fill="var(--teal)"/>
    </svg>

    <div class="brand">
      <span class="brand__dot"></span>
      <span class="brand__name">BRAVEL ACRES</span>
    </div>

    <p class="site">WWW.BRAVELACRES.COM</p>
  </section>

</main>
</body>
</html>
```